Sundial Bail Bonds Signboard Ad

I need a signboard ad that will be posted at a jail. We are a bail bond company and we bail people out of jail. The inmate/customer will call our company when they see our signboard ad posted inside a jail. The goal of the signboard ad is to get the attention of a person in custody and to stand out from the competition. The signboard ad is about 5x7. Open to any colors that will make it stand out. The content of the signboard ad must have "Sundial Bail Bonds" and our company phone number: (555) 318-2746. We want to emphasize we can get them out of jail quick and fast, was thinking maybe a catch phrase of "Sundial outta Jail" or "Sundial to Freedom". We don't have a logo. I will upload an attachment to show what the competition looks like. As you will see in the upload, my ad will go along with my competition. Also, I'm open to any creative ideas that will make my signboard ad stand out. Thank You.

Target Market(s)

People in jail.

Requirements
Must have
• Sundial Bail Bonds

(555) 318-2746
Nice to have
• I'm open to catch phrases that will get attention, for example "Sundial outta Jail" or "Sundial to Freedom". I do not have a company logo, if you can create a company logo, would be nice, was thinking an image of a rocket blasting off, The name of company is Sundial Bail Bonds.

```html
<!DOCTYPE html>
<html lang="en">
<head>
<meta charset="utf-8">
<title>Sundial Bail Bonds Signboard</title>
<link rel="stylesheet" href="https://fonts.googleapis.com/css2?family=Barlow+Condensed:wght@800&display=swap">
<style>
  :root {
    --backdrop: #000000;
    --sign-black: #1d1d1f;
    --blue-deep: #1f8fd0;
    --blue-mid: #4a9ad8;
    --blue-pale: #d6e6f6;
    --ink: #0a0a0c;
    --paper: #ffffff;
  }
  html, body {
    margin: 0;
    padding: 0;
    width: 1200px;
    height: 934px;
    overflow: hidden;
    background: var(--backdrop);
  }
  .signboard {
    display: block;
    width: 1200px;
    height: 934px;
  }
  .company-name {
    font-family: "Barlow Condensed", "Arial Narrow", sans-serif;
    font-weight: 800;
    font-size: 206px;
    fill: var(--paper);
  }
  .phone {
    font-family: "Barlow Condensed", "Arial Narrow", sans-serif;
    font-weight: 800;
    font-size: 176px;
    fill: var(--ink);
  }
</style>
</head>
<body>
<svg class="signboard" viewBox="0 0 1200 934" xmlns="http://www.w3.org/2000/svg" role="img" aria-label="Sundial Bail Bonds sign with phone number (555) 318-2746">
  <defs>
    <linearGradient id="blueField" x1="0" y1="1" x2="1" y2="0">
      <stop offset="0" stop-color="var(--blue-pale)"/>
      <stop offset="0.45" stop-color="var(--blue-mid)"/>
      <stop offset="1" stop-color="var(--blue-deep)"/>
    </linearGradient>
    <linearGradient id="footStripe" x1="0" y1="0" x2="1" y2="0">
      <stop offset="0" stop-color="#ffffff"/>
      <stop offset="1" stop-color="#7aaee0"/>
    </linearGradient>
    <clipPath id="signClip"><rect x="133" y="133" width="934" height="667"/></clipPath>
  </defs>

  <g class="sign" clip-path="url(#signClip)">
    <rect class="field" x="133" y="133" width="934" height="667" fill="url(#blueField)"/>
    <polygon class="sheen" points="133,200 520,580 470,580 133,250" fill="#ffffff" opacity="0.35"/>
    <polygon class="sheen" points="470,133 900,580 780,580 360,133" fill="#ffffff" opacity="0.12"/>
    <polygon class="sheen" points="133,330 380,580 133,580" fill="#ffffff" opacity="0.25"/>
    <polygon class="dark-corner" points="604,133 1067,133 1067,596" fill="var(--sign-black)"/>
    <line class="corner-edge" x1="590" y1="133" x2="1067" y2="610" stroke="var(--paper)" stroke-width="6"/>
    <polygon class="phone-band" points="133,586 1024,586 1067,628 1067,780 133,780" fill="var(--paper)" stroke="var(--sign-black)" stroke-width="3"/>
    <rect class="foot-stripe" x="133" y="786" width="934" height="14" fill="url(#footStripe)"/>
  </g>

  <g class="company-name">
    <text x="176" y="356" textLength="856" lengthAdjust="spacingAndGlyphs">SUNDIAL</text>
    <text x="176" y="528" textLength="856" lengthAdjust="spacingAndGlyphs">BAIL BONDS</text>
  </g>

  <text class="phone" x="174" y="742" textLength="808" lengthAdjust="spacingAndGlyphs">(555) 318-2746</text>
</svg>
</body>
</html>
```